Brindle Industries - Quality Campaign

Objective:

Create a visually engaging graphic design that promotes quality awareness and engagement within Brindle Industries. The design should convey the core values of quality at Brindle, emphasizing its four key elements:

Zero Defects, Zero Scrap
Customer Satisfaction
First Time Right
Product Performance
Target Audience:

Brindle Industries employees at all levels.

Usage:

The design will be used for various purposes, including:

Posters displayed in common areas and workstations
Presentation slides for internal meetings and training sessions
Design Requirements:

Visual Style: The design should be modern, professional, and visually appealing. It should evoke a sense of pride in quality and inspire team members to strive for excellence.
Color Palette: Consider using the Brindle Industries brand colors or a complementary palette that reflects quality and professionalism (see website: https://www.brindle-industries.example/).
Key Elements: The four key elements of quality should be clearly visible and integrated into the design. This could be achieved through text, icons, or a combination of both.
Brindle Industries Logo: A vector file of the Brindle Industries logo will be provided. Optional use of the logo is encouraged to maintain brand consistency.
Call to Action: The design should include a clear call to action, such as "Embrace Quality," "Strive for Excellence," or "Own Your Quality."
Additional Considerations:

Versatility: The design should be adaptable for different formats and sizes (e.g., posters, presentations, social media posts).
Memorability: The design should be memorable and easily recognizable as representing Brindle Industries' commitment to quality.
Deliverables:

High-resolution digital files in various formats suitable for printing and digital use.
By adhering to these guidelines, the winning design will effectively communicate the importance of quality at Brindle Industries and inspire employees to embrace these values in their daily work.

Industry/Entity Type

Engineering, manufacturing, semi-conductor, optics

Requirements
Must have
• Reference to Quality and 4 key elements

```html
<!DOCTYPE html>
<html lang="en">
<head>
<meta charset="utf-8">
<title>Brindle Industries – Core Values of Quality</title>
<link rel="stylesheet" href="https://fonts.googleapis.com/css2?family=Roboto:wght@400;500;700;900&display=swap">
<style>
  :root{
    --backdrop:#a19fa0;
    --paper:#ffffff;
    --ink:#060709;
    --blue-edge:#4f8acb;
    --blue-mid:#55aadf;
    --accent:#3aa6e0;
    --silver:#c9c9cb;
    --photo-cream:#ece7da;
    --photo-steel:#9da4b8;
  }
  *{margin:0;padding:0;box-sizing:border-box}
  html,body{width:1200px;height:1200px;overflow:hidden;background:var(--backdrop);font-family:"Roboto",Arial,sans-serif}
  .poster{position:absolute;left:231px;top:83px;width:738px;height:1034px;background:var(--paper);overflow:hidden}
  .hero-photo{position:absolute;left:0;top:0;width:738px;height:460px;
    background:
      radial-gradient(ellipse 300px 200px at 600px 120px, rgba(90,100,150,.55), transparent 70%),
      linear-gradient(180deg, var(--photo-cream) 0%, rgba(236,231,218,.7) 45%, rgba(255,255,255,0) 100%),
      linear-gradient(90deg, rgba(255,255,255,.9) 0%, var(--photo-steel) 100%);
  }
  .brand{position:absolute;left:23px;top:23px;display:flex;align-items:center;gap:12px}
  .brand-mark{width:52px;height:52px;background:var(--ink)}
  .brand-name{font-weight:400;font-size:33px;line-height:34px;color:var(--ink)}
  .frame{position:absolute;left:28px;top:228px;width:682px;height:682px;border:4px solid var(--ink);background:var(--paper)}
  .frame::before{content:"";position:absolute;inset:7px;border:1px solid var(--ink)}
  .quad{position:absolute;width:291px;height:291px;
    background:linear-gradient(180deg,var(--blue-edge) 0%,var(--blue-mid) 55%,var(--blue-edge) 100%)}
  .quad.tl{left:35px;top:34px}
  .quad.tr{left:348px;top:34px}
  .quad.bl{left:35px;top:348px;background:linear-gradient(0deg,var(--blue-edge) 0%,var(--blue-mid) 55%,var(--blue-edge) 100%)}
  .quad.br{left:348px;top:348px;background:linear-gradient(0deg,var(--blue-edge) 0%,var(--blue-mid) 55%,var(--blue-edge) 100%)}
  .value{position:absolute;font-weight:700;font-size:32px;line-height:37px;color:var(--ink)}
  .quad.tl .value{left:43px;top:120px}
  .quad.tr .value{right:47px;top:120px;text-align:right}
  .quad.bl .value{left:43px;top:100px}
  .quad.br .value{right:47px;top:100px;text-align:right}
  .badge{position:absolute;width:103px;height:103px;background:var(--ink);box-shadow:0 0 0 3px var(--accent)}
  .badge svg{width:103px;height:103px;display:block}
  .badge.tl{left:26px;top:25px}
  .badge.tr{left:545px;top:25px}
  .badge.bl{left:26px;top:544px}
  .badge.br{left:545px;top:544px}
  .core{position:absolute;left:214px;top:214px;width:246px;height:246px;border-radius:50%;
    background:radial-gradient(circle at 50% 40%,#fafafa 0%,var(--silver) 70%,#8f9092 100%);
    box-shadow:0 4px 10px rgba(0,0,0,.35)}
  .core-inner{position:absolute;inset:13px;border-radius:50%;background:var(--ink);
    display:flex;align-items:center;justify-content:center;text-align:center;
    color:#fff;font-weight:700;font-size:34px;line-height:37px}
  .footer-band{position:absolute;left:0;top:954px;width:738px;height:80px;background:var(--ink)}
  .footer-rule{position:absolute;left:22px;top:35px;width:395px;height:2px;background:#fff}
  .call-to-action{position:absolute;left:432px;top:18px;color:#fff;font-weight:700;font-size:28px;letter-spacing:3.6px;white-space:nowrap}
</style>
</head>
<body>
<main class="poster">
  <div class="hero-photo" role="img" aria-label="Faded photograph of lab test equipment with an oscilloscope screen showing a signal trace"></div>

  <header class="brand">
    <span class="brand-mark"></span>
    <span class="brand-name">Brindle<br>Industries</span>
  </header>

  <section class="frame">
    <div class="quad tl"><p class="value">Zero Defects,<br>Zero Scrap</p></div>
    <div class="quad tr"><p class="value">Customer<br>Satisfaction</p></div>
    <div class="quad bl"><p class="value">First Time<br>Right</p></div>
    <div class="quad br"><p class="value">Product<br>Performance</p></div>

    <div class="badge tl">
      <svg viewBox="0 0 103 103" aria-hidden="true">
        <circle cx="46" cy="48" r="24" fill="none" stroke="#fff" stroke-width="7" stroke-dasharray="7 5"/>
        <circle cx="46" cy="48" r="17" fill="none" stroke="#fff" stroke-width="3"/>
        <line x1="34" y1="60" x2="58" y2="36" stroke="#fff" stroke-width="3"/>
        <circle cx="72" cy="74" r="11" fill="#fff" stroke="#060709" stroke-width="2"/>
        <path d="M66 74l4 4 8-8" fill="none" stroke="#060709" stroke-width="3"/>
      </svg>
    </div>
    <div class="badge tr">
      <svg viewBox="0 0 103 103" aria-hidden="true">
        <g fill="#fff">
          <polygon points="51,22 54,29 61,29 55,33 57,40 51,36 45,40 47,33 41,29 48,29"/>
          <polygon points="34,28 36,33 41,33 37,36 38,41 34,38 30,41 31,36 27,33 32,33"/>
          <polygon points="68,28 70,33 75,33 71,36 72,41 68,38 64,41 65,36 61,33 66,33"/>
          <polygon points="22,40 24,45 29,45 25,48 26,53 22,50 18,53 19,48 15,45 20,45"/>
          <polygon points="80,40 82,45 87,45 83,48 84,53 80,50 76,53 77,48 73,45 78,45"/>
          <circle cx="51" cy="53" r="8"/>
          <path d="M36 76c0-10 7-14 15-14s15 4 15 14z"/>
        </g>
        <circle cx="72" cy="72" r="11" fill="#fff" stroke="#060709" stroke-width="2"/>
        <path d="M66 72l4 4 8-8" fill="none" stroke="#060709" stroke-width="3"/>
      </svg>
    </div>
    <div class="badge bl">
      <svg viewBox="0 0 103 103" aria-hidden="true">
        <path d="M70 72A29 29 0 1 1 76 42" fill="none" stroke="#fff" stroke-width="4"/>
        <path d="M70 46l6 8 6-8z" fill="#fff"/>
        <text x="48" y="61" fill="#fff" font-family="Georgia,serif" font-size="34" text-anchor="middle">1</text>
        <circle cx="74" cy="76" r="11" fill="#fff" stroke="#060709" stroke-width="2"/>
        <path d="M68 76l4 4 8-8" fill="none" stroke="#060709" stroke-width="3"/>
      </svg>
    </div>
    <div class="badge br">
      <svg viewBox="0 0 103 103" aria-hidden="true">
        <circle cx="48" cy="33" r="15" fill="none" stroke="#fff" stroke-width="6" stroke-dasharray="5 4"/>
        <rect x="22" y="36" width="52" height="48" fill="#fff"/>
        <path d="M40 36v20l8-6 8 6V36" fill="none" stroke="#060709" stroke-width="3"/>
        <circle cx="72" cy="76" r="11" fill="#fff" stroke="#060709" stroke-width="2"/>
        <path d="M66 76l4 4 8-8" fill="none" stroke="#060709" stroke-width="3"/>
      </svg>
    </div>

    <div class="core"><div class="core-inner">The<br>Core Values<br>of<br>Quality</div></div>
  </section>

  <footer class="footer-band">
    <span class="footer-rule"></span>
    <p class="call-to-action">Own Your Quality</p>
  </footer>
</main>
</body>
</html>
```